Professional & attention grabbing.

A business card design, front and back. I already have a logo I will attach, but I am open to something new as well.
Things to include:
Name:
Title:
Phone:
Email:
Wanting something that is professional but attention grabbing.
Also we do a lot of work using drones on natural gas pipelines (leading the future)if you want to include any of that. I'm open to ideas.
Target Market(s)
Natural gas transmission industry / greenhouse gas mitigation industry
Industry/Entity Type
Business
Contact Information for Business Card
All details have been conveyed above.
Colors
Designer to choose colors to be used in the design.
Look and feel
Each slider illustrates characteristics of the customer's brand and the style your logo design should communicate.

```html
<!DOCTYPE html>
<html lang="en">
<head>
<meta charset="utf-8">
<title>Kestrel Field Inspections — Business Card</title>
<link href="https://fonts.googleapis.com/css2?family=Montserrat:wght@400;600;800&display=swap" rel="stylesheet">
<style>
  :root {
    --backdrop: #e9eaec;
    --card: #ffffff;
    --ink: #2b2b2d;
    --muted: #5a5a5e;
    --accent: #d3202b;
  }
  * { margin: 0; padding: 0; box-sizing: border-box; }
  html, body { width: 1200px; height: 900px; overflow: hidden; }
  body {
    background: var(--backdrop);
    font-family: "Montserrat", Arial, sans-serif;
    color: var(--ink);
    display: flex;
    flex-direction: column;
    align-items: center;
    justify-content: center;
    gap: 56px;
  }
  .card {
    position: relative;
    width: 560px;
    height: 320px;
    background: var(--card);
    box-shadow: 0 10px 30px rgba(0,0,0,.12);
    overflow: hidden;
  }
  .bar {
    position: absolute;
    height: 22px;
    background: var(--accent);
  }
  .bar--top { top: 42px; left: 0; width: 120px; }
  .bar--bottom { bottom: 42px; right: 0; width: 120px; }

  .brand {
    display: flex;
    align-items: center;
    gap: 12px;
  }
  .brand__square {
    width: 24px; height: 24px;
    background: var(--accent);
    flex: none;
  }
  .brand__name {
    font-weight: 800;
    font-size: 24px;
    letter-spacing: .3px;
    color: var(--ink);
    line-height: 1.15;
    white-space: nowrap;
  }

  /* back: brand side */
  .card--brand .brand {
    position: absolute;
    top: 50%; left: 50%;
    transform: translate(-50%, -50%);
  }

  /* front: contact side */
  .card--contact .brand {
    position: absolute;
    left: 40px; top: 108px;
  }
  .card--contact .brand__name { font-size: 21px; }
  .contact {
    position: absolute;
    left: 312px; top: 92px;
  }
  .contact__name {
    font-weight: 800;
    font-size: 22px;
    color: var(--accent);
  }
  .contact__title {
    font-size: 15px;
    color: var(--muted);
    margin: 2px 0 14px;
  }
  .contact__list { list-style: none; }
  .contact__item {
    display: flex;
    align-items: center;
    gap: 10px;
    font-size: 13px;
    color: var(--muted);
    margin-bottom: 7px;
    white-space: nowrap;
  }
  .contact__icon { width: 16px; height: 16px; flex: none; }
</style>
</head>
<body>

  <section class="card card--brand" aria-label="Card back">
    <div class="bar bar--top"></div>
    <div class="brand">
      <span class="brand__square"></span>
      <span class="brand__name">Kestrel Field Inspections</span>
    </div>
    <div class="bar bar--bottom"></div>
  </section>

  <section class="card card--contact" aria-label="Card front">
    <div class="bar bar--top"></div>
    <div class="brand">
      <span class="brand__square"></span>
      <span class="brand__name">Kestrel<br>Field Inspections</span>
    </div>
    <div class="contact">
      <h1 class="contact__name">Daniel Marsh</h1>
      <p class="contact__title">Title</p>
      <ul class="contact__list">
        <li class="contact__item">
          <svg class="contact__icon" viewBox="0 0 16 16"><circle cx="8" cy="8" r="7.5" fill="none" stroke="#d3202b"/><path d="M5.5 4.5l1.5 0 .6 2-1 .8a5 5 0 0 0 2 2l.8-1 2 .6v1.5c-3.5.3-6.2-2.4-5.9-5.9z" fill="#d3202b"/></svg>
          555-014-2290
        </li>
        <li class="contact__item">
          <svg class="contact__icon" viewBox="0 0 16 16"><circle cx="8" cy="8" r="7.5" fill="none" stroke="#d3202b"/><rect x="4" y="5.5" width="8" height="5.5" fill="none" stroke="#d3202b"/><path d="M4 5.5l4 3 4-3" fill="none" stroke="#d3202b"/></svg>
          yourname@example.com
        </li>
        <li class="contact__item">
          <svg class="contact__icon" viewBox="0 0 16 16"><circle cx="8" cy="8" r="7.5" fill="#d3202b"/><path d="M8 3.8a2.6 2.6 0 0 0-2.6 2.6C5.4 8.4 8 12 8 12s2.6-3.6 2.6-5.6A2.6 2.6 0 0 0 8 3.8z" fill="#fff"/><circle cx="8" cy="6.4" r="1" fill="#d3202b"/></svg>
          your street address here
        </li>
        <li class="contact__item">
          <svg class="contact__icon" viewBox="0 0 16 16"><circle cx="8" cy="8" r="7.5" fill="none" stroke="#d3202b"/><circle cx="8" cy="8" r="4" fill="none" stroke="#d3202b"/><path d="M4 8h8M8 4c-1.5 1.2-1.5 6.8 0 8M8 4c1.5 1.2 1.5 6.8 0 8" fill="none" stroke="#d3202b" stroke-width=".8"/></svg>
          www.your wesite name
        </li>
      </ul>
    </div>
    <div class="bar bar--bottom"></div>
  </section>

</body>
</html>
```